Glanvero foot health or foot health glanvero

Treatments in comfort of your own home
Delia Marsh cert KTRVb Pod, LQNDoct
Treatments will be listed on the leaflet I will attach
I am a Foot Health practitioner,
I want to mention I do home visits throughout Pembrokeshire & Ceredigion.
Tel. 07604519283
I have 2 logs to forward to you they are the associations I belong to .
One of which is also a certification mark. It is important that the same colour is used for this mark. They are not the main focus, they are just recognised mark. To be at the top or bottom of the page.
There is a local business called Tregarrow foot clinic, so my business has to be glanvero foot health, or foot health glanvero
soon I will also need a web page and cards designed, so please keep this in mind when designing the Artwork. I will also need an email on the leaflet but I will wait and see what the design is first before I confirm it as I have several.
I hope this is enough info for you.
Many thanks,
Delia Marsh

Target Market(s)

Mostly the elderly, some middle age women, but it is a service for all ages. The elderly are my main clients.

Industry/Entity Type

Health

Font styles to use
Serif
Sans Serif

Colors

Designer to choose colors to be used in the design.

Requirements
Must have
• Covering Pembrokeshire & Ceredigion.
Treatments include:- as listed on example leaflet I sent
Phone number a size that's easily readable.
I am open to colours. I love bright colours, but also like the more conservative colours as long as it looks professional. I'm wanting it to look more up market.
Nice to have
• Logo for Guildhall and KTE logo obviously smaller, but also recognisable and either at the top of page or bottom. These are not to be main focal point.

```html
<!DOCTYPE html>
<html lang="en">
<head>
<meta charset="utf-8">
<title>Glanvero Foothealth – Leaflet</title>
<link rel="stylesheet" href="https://fonts.googleapis.com/css2?family=Lobster&family=Noto+Serif:ital,wght@0,400;0,700;1,400;1,700&display=swap">
<style>
  :root {
    --cream: #fde8cb;
    --peach-edge: #f6a552;
    --brown-dark: #5a1f0c;
    --brown-band-1: #5e3514;
    --brown-band-2: #7a4a22;
    --gold: #c98a14;
    --gold-light: #e9b23a;
    --text-cream: #fbefdc;
    --text-brown: #6a3f12;
    --ornament: #f1d9a8;
    --ornament-gold: #d59a2c;
    --register-purple: #5b3fc4;
    --guild-green: #2f6b3a;
  }
  * { margin: 0; padding: 0; box-sizing: border-box; }
  html, body { width: 846px; height: 1200px; overflow: hidden; }
  body { background: var(--peach-edge); }

  .leaflet {
    position: relative;
    width: 846px;
    height: 1200px;
    overflow: hidden;
    background: radial-gradient(ellipse 75% 70% at 50% 50%, var(--cream) 55%, #fbcf95 85%, var(--peach-edge) 100%);
    font-family: "Noto Serif", Georgia, serif;
  }

  .ornament { position: absolute; border-radius: 40% 60% 50% 50%; }
  .ornament--top-left { left: 18px; top: 18px; width: 150px; height: 240px;
    background: radial-gradient(circle at 30% 25%, rgba(213,154,44,.45), rgba(213,154,44,0) 70%); }
  .ornament--band-right { left: 645px; top: 320px; width: 200px; height: 170px;
    background: radial-gradient(circle at 60% 50%, rgba(241,217,168,.75), rgba(241,217,168,0) 70%); }
  .ornament--band-left { left: 0; top: 752px; width: 230px; height: 150px;
    background: radial-gradient(circle at 40% 45%, rgba(241,217,168,.75), rgba(241,217,168,0) 70%); }
  .ornament--bottom-right { left: 600px; top: 935px; width: 230px; height: 245px;
    background: radial-gradient(circle at 75% 75%, rgba(213,154,44,.45), rgba(213,154,44,0) 70%); }

  .brand { position: absolute; top: 92px; left: 0; width: 846px; text-align: center; font-family: "Lobster", cursive; }
  .brand__name { display: block; font-size: 74px; line-height: 78px; color: var(--brown-dark);
    text-shadow: 1px 2px 2px rgba(90,31,12,.35); }
  .brand__sub { display: block; font-size: 74px; line-height: 76px; color: var(--gold);
    text-shadow: 1px 2px 2px rgba(120,70,10,.35); }

  .divider { position: absolute; left: 162px; top: 265px; width: 520px; height: 1px; background: #c9a677; }

  .tagline { position: absolute; top: 280px; width: 846px; text-align: center;
    font-style: italic; font-size: 23px; color: var(--text-brown); }

  .treatments { position: absolute; left: 0; top: 347px; width: 846px; height: 413px;
    background: var(--brown-band-1); box-shadow: 0 3px 6px rgba(60,20,0,.3); }
  .treatments__title { height: 78px; line-height: 82px; text-align: center;
    font-family: "Lobster", cursive; font-size: 40px; color: #f6d9a0;
    background: linear-gradient(#5a3110, #6a3c16); }
  .treatments__list { list-style: none; }
  .treatments__item { height: 56px; line-height: 54px; text-align: center; font-size: 29px;
    color: var(--text-cream); text-shadow: 1px 1px 2px rgba(0,0,0,.4); }
  .treatments__item:nth-child(odd) { background: var(--brown-band-2); }
  .treatments__item:nth-child(even) { background: var(--brown-band-1); }

  .coverage { position: absolute; left: 0; top: 760px; width: 846px; height: 78px;
    background: linear-gradient(#b9770f, var(--gold-light) 50%, #b9770f);
    text-align: center; padding-top: 8px;
    font-weight: 700; font-style: italic; font-size: 25px; line-height: 31px; color: #fff8ea;
    text-shadow: 1px 1px 2px rgba(80,40,0,.6); }

  .contact { position: absolute; right: 128px; top: 880px; text-align: right; }
  .contact__name { font-family: "Lobster", cursive; font-size: 48px; line-height: 56px; color: var(--brown-dark); }
  .contact__creds { font-family: "Lobster", cursive; font-size: 30px; line-height: 38px; color: var(--gold); }
  .contact__role { font-style: italic; font-size: 27px; line-height: 36px; color: var(--text-brown); }
  .contact__phone { font-size: 50px; line-height: 60px; font-weight: 700; font-style: italic; color: #4a2a0c; letter-spacing: 1px; }
  .contact__note { font-style: italic; font-size: 23px; line-height: 30px; color: var(--text-brown); }

  .badge { position: absolute; }
  .badge--guild { left: 52px; top: 1015px; width: 140px; height: 95px; border-radius: 50%; background: var(--guild-green); }
  .badge--register { left: 222px; top: 1045px; width: 44px; height: 44px; border-radius: 50%; background: var(--register-purple); }
</style>
</head>
<body>
<main class="leaflet">
  <div class="ornament ornament--top-left" role="img" aria-label="Gold grapevine corner flourish"></div>
  <div class="ornament ornament--band-right" role="img" aria-label="Cream scroll ornament"></div>
  <div class="ornament ornament--band-left" role="img" aria-label="Cream scroll ornament"></div>
  <div class="ornament ornament--bottom-right" role="img" aria-label="Gold grapevine corner flourish"></div>

  <h1 class="brand">
    <span class="brand__name">Glanvero</span>
    <span class="brand__sub">Foothealth</span>
  </h1>
  <div class="divider"></div>
  <p class="tagline">Treatments in comfort of your own home</p>

  <section class="treatments">
    <h2 class="treatments__title">Treatments Include:</h2>
    <ul class="treatments__list">
      <li class="treatments__item">Diabetic Footcare</li>
      <li class="treatments__item">Ingrowing Toenails</li>
      <li class="treatments__item">Corn &amp; Callous Treatment</li>
      <li class="treatments__item">Toenail Clipping</li>
      <li class="treatments__item">Fungal Infections Treated</li>
      <li class="treatments__item">Cracked Heels</li>
    </ul>
  </section>

  <p class="coverage">Home visits throughout<br>Pembrokeshire &amp; Ceredigion.</p>

  <section class="contact">
    <p class="contact__name">Delia Marsh</p>
    <p class="contact__creds">cert .KTRVb Pod, LQNDoct</p>
    <p class="contact__role">Foot Health practitioner</p>
    <p class="contact__phone">076 0451 9283</p>
    <p class="contact__note">Home visit by Arragement</p>
  </section>

  <div class="badge badge--guild" role="img" aria-label="Guildhall membership badge"></div>
  <div class="badge badge--register" role="img" aria-label="KTE certification mark"></div>
</main>
</body>
</html>
```